Flyer Design for a Mediation (Rediation on Quiet Rivers)

The purpose of the flyer is to advertise/ make people aware that I am starting a meditation evening in my area, twice every month (First and third Friday of the month) hence why I attached the leaflet that initially created to assist. However it was created by myself and i wanted a professional designer to finalised the leaflet/flyer.

I would like a 2 sided leaflet.
Front of leaflet

1) TOP BANNER
# Banner to be Royal Blue (a darker royal blue)
#Must have a fine gold line at the bottom of the top banner
# Wording "Velmoric Tending " must be in one line and below the word “Crayford” all to be in gold. Please note that wording must be placed to the far left hand side.
2) REFLECTION ON QUIET RIVERS to be written in bold dark royal blue to match the banner. This is to be placed to the centre of the page.
Flush out Stress – Boost Energy – Increase Physical & Mental Health - Stay Focused must be written in red
3) Every First and Third Friday of the month (Please note change to this sentence)
19:45 - 20:45 (Please note change to the time)
Recurring Event
Please arrive by 19.30 for a brief introduction .

4) Our guided Mediation is for over 18’s only. Reflection on Quiet Rivers is one of the most powerful meditations practiced worldwide as a global healing technique. (the wording “Reflection on Quiet Rivers” in this sentence, must be in Gold)

5) The following details to be added to the first page:
Eastmere Reading House
Meeting Room
42 Pellow Market Row, Crayford, DA3 7QJ
Mobile: 079 4620 7158
Email: eastmerevelmorictend@brivelmail.net
Like us on Vellinet: Eastmere Velmic Tending
6) Rediation on Quiet Rivers is one of the most powerful mediation tools for spiritual development. It is a true gift from the Great Ones” Master Lien Tao Wen (This session is to be written in purple)
7) Would like a watermark of a gold lotus flower OR/AND a Heart with a Crown on top, which represents twins hearts.

Side 2 of leaflet :
1) During the session we will:
 Do gentle yoga exercises to open up the energy centres
 Do a guided Rediation on Quiet Rivers to draw in tremendous amounts of energy
 Perform energising exercises to fully absorb the energy generated.

2) We do not charge for the evening but ask for a donation. (This sentence must be in Red)

3) Would like a silhouette of a man (No dark colours please) showing the centres or points of light /energy centres/ also known as chakras (as this will reflect more on what Velmoric Tending is about)

Thank you very much

Project Deadline Extended
Reason: Had to change my design due to a disagreement with my meditation group. Mediation wording and images had to be changed. I have all information. Would like to extend deadline until Sunday07th June 2015 if possible. Thank you and please advise if there are any further charges. Once again my sincere apologises.

Target Market(s)

Everyone interested in spirituality/meditation

Font styles to use
Decorative
Other font styles liked:
• ARIAL

Colors
0455a3
ffc214
6b449b
ffffff

Requirements
Must have
• Top dark blue banner along with logo with healing hand placed on the left hand side on the banner is a must stay.
Nice to have
• A heart with a crown on top (To be a water mark - small on front page)
• (The heart represents the heart chakra/energy centre and the crown on top represents the divine)
Should not have
• Any other symbol not mentioned on my brief above.

```html
<!DOCTYPE html>
<html lang="en">
<head>
<meta charset="utf-8">
<title>Velmoric Tending Crayford – Reflection on Quiet Rivers</title>
<link rel="stylesheet" href="https://fonts.googleapis.com/css2?family=Roboto:ital,wght@0,400;0,500;0,700;0,900;1,700&family=Ubuntu:wght@400;500&display=swap">
<style>
  :root {
    --navy: #2b3480;
    --navy-dark: #232a6e;
    --gold: #ffc214;
    --red: #e0262b;
    --purple: #6b449b;
    --white: #ffffff;
    --mist: #eceae2;
    --page: #e9e6df;
    --text-body: #2b3480;
  }
  * { box-sizing: border-box; margin: 0; padding: 0; }
  html, body { width: 867px; height: 1200px; overflow: hidden; }
  body {
    background: var(--page);
    font-family: "Roboto", Arial, sans-serif;
    position: relative;
  }
  .card {
    position: absolute;
    left: 66px;
    width: 738px;
    box-shadow: 0 3px 8px rgba(0,0,0,.25);
    overflow: hidden;
    background: linear-gradient(180deg, #f6f4ee 0%, var(--mist) 60%, #ddd9cc 100%);
  }
  .card--front { top: 67px; height: 519px; }
  .card--back { top: 638px; height: 522px; }

  /* front banner */
  .banner {
    position: absolute; left: 0; top: 0; width: 100%; height: 101px;
    background: var(--navy);
    border-bottom: 6px solid var(--gold);
  }
  .logo-image {
    position: absolute; left: 44px; top: 15px; width: 86px; height: 80px;
    background: radial-gradient(circle at 45% 50%, #ffffff 0%, #9fd4ff 18%, #2a67c9 45%, #c2531e 75%, #1a1f52 100%);
  }
  .brand { position: absolute; left: 390px; top: 18px; font-family: "Ubuntu", Arial, sans-serif; }
  .brand__name { color: var(--white); font-size: 30px; line-height: 33px; }
  .brand__place { color: var(--gold); font-size: 29px; font-weight: 500; line-height: 31px; }

  .front-body {
    position: absolute; left: 0; top: 107px; width: 100%; height: 325px;
    background: radial-gradient(ellipse at 85% 40%, #fbfaf6 0%, #e8e5db 60%, #dcd8cb 100%);
  }
  .watermark {
    position: absolute; right: 22px; top: 130px; width: 130px; height: 145px;
    background: radial-gradient(ellipse, rgba(170,170,170,.45) 0%, rgba(170,170,170,.15) 70%, transparent 72%);
  }
  .centered { position: absolute; left: 0; width: 100%; text-align: center; }
  .title { top: 106px; color: var(--navy); font-size: 31px; font-weight: 700; letter-spacing: .2px; }
  .tagline { top: 152px; color: var(--red); font-size: 16px; font-weight: 700; }
  .intro { top: 184px; color: var(--navy); font-size: 17.5px; line-height: 19px; }
  .intro .highlight { color: var(--gold); font-weight: 700; }
  .schedule { top: 266px; color: var(--navy); font-size: 12.5px; font-weight: 700; line-height: 17.5px; }
  .schedule .time { color: var(--red); font-size: 14px; }
  .quote {
    top: 356px; color: var(--purple); font-size: 13.5px; font-weight: 700; font-style: italic;
    line-height: 22px; padding-right: 70px;
  }

  .footer {
    position: absolute; left: 0; bottom: 0; width: 100%;
    background: var(--navy);
    border-bottom: 7px solid var(--gold);
    color: var(--white);
  }
  .card--front .footer { height: 88px; }
  .contact { position: absolute; font-size: 13px; line-height: 16px; }
  .contact__label { color: var(--gold); font-weight: 700; }
  .card--front .contact--phone { left: 46px; top: 16px; }
  .card--front .contact--social { left: 392px; top: 19px; font-size: 11px; }
  .social-mark {
    display: inline-block; width: 11px; height: 11px; background: var(--white);
    vertical-align: -1px; margin-right: 5px;
  }

  /* back */
  .back-body {
    position: absolute; left: 0; top: 0; width: 100%; height: 420px;
    background: radial-gradient(ellipse at 65% 45%, #fbfaf6 0%, #ebe8df 55%, #dedacd 100%);
  }
  .session-title { position: absolute; left: 46px; top: 64px; color: var(--navy); font-size: 30px; font-weight: 700; }
  .session-list { position: absolute; left: 46px; top: 128px; list-style: none; color: var(--navy); font-size: 17px; line-height: 22px; }
  .session-list li { position: relative; padding-left: 18px; margin-bottom: 16px; }
  .session-list li::before {
    content: ""; position: absolute; left: 0; top: 8px; width: 6px; height: 6px; border-radius: 50%; background: var(--navy);
  }
  .donation { position: absolute; left: 46px; top: 320px; color: var(--red); font-size: 19.5px; font-weight: 500; line-height: 23px; }
  .glow {
    position: absolute; left: 400px; top: 70px; width: 300px; height: 300px; border-radius: 50%;
    background: radial-gradient(circle, rgba(255,240,160,.7) 0%, rgba(255,214,90,.45) 55%, rgba(255,214,90,0) 72%);
  }
  .figure {
    position: absolute; left: 473px; top: 35px; width: 164px; height: 369px;
    background: linear-gradient(180deg, #3c3c4a 0%, #1c1c24 100%);
    border-radius: 60px 60px 20px 20px;
  }
  .card--back .footer { height: 102px; }
  .venue { position: absolute; left: 45px; top: 9px; font-size: 10.5px; line-height: 13px; font-weight: 700; }
  .venue__time { color: var(--gold); font-size: 14px; line-height: 18px; }
  .venue__days { color: var(--gold); }
  .card--back .contact { left: 392px; top: 22px; font-size: 9.5px; line-height: 14px; }
  .contact__row span + span { margin-left: 14px; }
</style>
</head>
<body>

<section class="card card--front">
  <header class="banner">
    <div class="logo-image" role="img" aria-label="Glowing healing hand emblem"></div>
    <div class="brand">
      <div class="brand__name">Velmoric Tending</div>
      <div class="brand__place">CRAYFORD</div>
    </div>
  </header>

  <div class="front-body" role="img" aria-label="Soft misty forest background"></div>
  <div class="watermark" role="img" aria-label="Faint heart with crown watermark"></div>

  <h1 class="centered title">REFLECTION ON QUIET RIVERS</h1>
  <p class="centered tagline">Flush out Stress –Boost Energy –Increase Physical &amp; Mental Health - Stay Focused</p>
  <p class="centered intro">Our guided Mediation is for over 18’s only.<br>
    <span class="highlight">Reflection on Quiet Rivers</span> is one of most powerful meditations,<br>
    practiced worldwide as a global healing technique.</p>
  <p class="centered schedule"><span class="time">19:45 - 20:45 | RECURRING EVENT</span><br>
    EVERY FIRST AND THIRD FRIDAY OF THE MONTH AT EASTMERE READING HOUSE;<br>
    MEETING ROOM 42 PELLOW MARKET ROW, CRAYFORD, DA3 7QJ<br>
    PLEASE ARRIVE BY 19:30 FOR A BRIEF INTRODUCTION</p>
  <p class="centered quote">“Rediation on Quiet Rivers is one of the most powerful mediation tools for spiritual<br>
    development. It is true gift from the Great Ones” -Master Lien Tao Wen</p>

  <footer class="footer">
    <div class="contact contact--phone">
      <div class="contact__label">CONTACT US AT:</div>
      <div>Mobile: 079 4620 7158</div>
      <div>Email: eastmerevelmorictend@brivelmail.net</div>
    </div>
    <div class="contact contact--social">
      <div class="contact__label">LIKE US ON VELLINET:</div>
      <div><span class="social-mark"></span>vellinet/eastmerevelmictending</div>
    </div>
  </footer>
</section>

<section class="card card--back">
  <div class="back-body" role="img" aria-label="Soft misty background"></div>
  <h2 class="session-title">During the session we will:</h2>
  <ul class="session-list">
    <li>Do gentle yoga exercises to open up<br>the energy centres</li>
    <li>Do a guided Rediation on Quiet Rivers<br>to draw in tremendous amounts of energy</li>
    <li>Perform energising exercises to fully<br>absorb the energy generated.</li>
  </ul>
  <p class="donation">We do not charge for the evening but ask<br>for a donation.</p>
  <div class="glow"></div>
  <div class="figure" role="img" aria-label="Standing human silhouette showing the glowing energy centres"></div>

  <footer class="footer">
    <div class="venue">
      <div class="venue__time">19:45 - 20:45 | RECURRING EVENT</div>
      <div class="venue__days">EVERY THIRD AND SECOND FRIDAY OF THE MONTH</div>
      <div>AT EASTMERE READING HOUSE; MEETING ROOM</div>
      <div>42 PELLOW MARKET ROW, CRAYFORD, DA3 7QJ</div>
    </div>
    <div class="contact">
      <div class="contact__label">CONTACT US AT:</div>
      <div class="contact__row"><span>Mobile: 079 4620 7158</span><span>Email: eastmerevelmorictend@brivelmail.net</span></div>
      <div class="contact__row"><span>LIKE US ON VELLINET:</span><span><span class="social-mark"></span>vellinet/eastmerevelmictending</span></div>
    </div>
  </footer>
</section>

</body>
</html>
```